Quorra Capital - Tailored Lending and Mortgage Solutions

Hi,

We need a brochure for a new mortgage broking company based in Sydney New South Wales. We act as mortgage brokers to assist clients find the most suitable loans. More details as follows:

1. We offer the following services:
• Mortgage solutions tailored to your needs
• Asset Finance solutions
• Commercial/business lending solutions
• We can conduct over the phone interviews to save you time
• We have access to a wide panel of lenders to save you time and do all the
legwork for you to save you time and money. We also do not charge a brokerage fee.
• We do not charge you a fee on top of standard bank fees and charges for using our services

Important to have 'Call us now for a borrowing capacity or email us your details and we will call within 24 hours'.

We need the colors to suit our logo in the attachment. Please also include our contact numbers, ABN 48213097564 and photograph. Please contact me should you have any questions.

Many thanks,
Tessa

Target Market(s)

Nationwide

Industry/Entity Type

Finance

Font styles to use
Serif

Requirements
Must have
• - My photograph and contact details.
• - Pictures relating to the topic
• - Business name and logo as per attachment
• - folds into front, middle and back page.
• - double sided layout
• 1. We offer the following services:
• • Mortgage solutions tailored to your needs
• • Asset Finance solutions
• • Commercial/business lending solutions
• • We can conduct over the phone interviews to save you time
• • We have access to a wide panel of lenders to save you time and do all the
• legwork for you to save you time and money. We also do not charge a brokerage fee.
• • We do not charge you a fee on top of standard bank fees and charges for using our services
• Important to have 'Call us now for a borrowing capacity or email us your details and we will call within 24 hours'.

```html
<!DOCTYPE html>
<html lang="en">
<head>
<meta charset="utf-8">
<title>Quorra Capital – Trifold Brochure</title>
<link href="https://fonts.googleapis.com/css2?family=Open+Sans:ital,wght@0,400;0,600;0,700;0,800;1,400&display=swap" rel="stylesheet">
<style>
  :root {
    --orange: #f39200;
    --orange-light: #f7b24a;
    --ink: #4a4a4a;
    --ink-soft: #7a7a7a;
    --paper: #ffffff;
    --canvas: #f2f2f2;
    --rule: #e3e3e3;
  }
  * { box-sizing: border-box; margin: 0; padding: 0; }
  html, body { width: 900px; height: 1200px; overflow: hidden; }
  body {
    background: var(--canvas);
    font-family: "Open Sans", Arial, sans-serif;
    color: var(--ink);
    position: relative;
  }
  .sheet {
    position: absolute;
    left: 30px;
    width: 840px;
    height: 570px;
    background: var(--paper);
    box-shadow: 0 3px 10px rgba(0,0,0,.18);
    display: flex;
    overflow: hidden;
  }
  .sheet--outside { top: 15px; }
  .sheet--inside { top: 615px; }
  .panel { position: relative; width: 280px; height: 100%; overflow: hidden; }
  .panel + .panel { border-left: 1px solid var(--rule); }
  .photo { position: absolute; display: block; }

  /* Outside – contact panel */
  .callout {
    position: absolute; top: 22px; left: 52px; right: 20px;
    font-size: 21px; line-height: 1.12; font-weight: 600; color: var(--ink);
    text-align: center;
  }
  .callout strong { color: var(--orange); font-weight: 800; }
  .contact-tab {
    position: absolute; left: 0; top: 360px; width: 38px; height: 210px;
    background: var(--orange);
  }
  .contact-tab span {
    position: absolute; left: 50%; top: 50%;
    transform: translate(-50%, -50%) rotate(-90deg);
    color: #fff; font-weight: 700; font-size: 20px; white-space: nowrap;
  }

  /* Outside – director panel */
  .portrait {
    position: absolute; left: 80px; top: 18px; width: 120px; height: 120px;
    border-radius: 50%; border: 4px solid var(--paper);
    box-shadow: 0 0 0 2px var(--orange);
    background: radial-gradient(circle at 50% 40%, #e8c2a6, #a0663e 70%);
  }
  .director { position: absolute; left: 0; right: 0; top: 232px; text-align: center; }
  .director__name { color: var(--orange); font-size: 22px; font-weight: 700; }
  .director__company { font-size: 16px; font-weight: 600; color: var(--ink); }
  .director__role { font-size: 13px; color: var(--ink-soft); }
  .detail {
    position: absolute; left: 0; right: 0; text-align: center;
    font-size: 11px; line-height: 1.5; color: var(--ink-soft);
  }
  .detail svg { display: block; margin: 0 auto 4px; }
  .detail--phone { top: 300px; }
  .detail--address { top: 365px; }
  .detail--email { top: 430px; }
  .detail--web { top: 498px; font-weight: 700; color: var(--ink); font-size: 12px; }

  /* Outside – cover panel */
  .brand {
    position: absolute; left: 0; right: 0; top: 418px;
    display: flex; align-items: center; justify-content: center; gap: 10px;
  }
  .brand__mark { width: 22px; height: 22px; background: var(--orange); }
  .brand__name { font-size: 24px; font-weight: 700; color: var(--orange); letter-spacing: .5px; }
  .brand__tagline {
    position: absolute; left: 0; right: 0; top: 454px; text-align: center;
    font-size: 9px; letter-spacing: 1px; text-transform: uppercase; color: var(--ink-soft);
  }
  .cover-swoosh { position: absolute; left: 0; bottom: 0; }

  /* Inside */
  .who {
    position: absolute; left: 0; top: 0; width: 100%; height: 290px;
    background: var(--orange); padding: 26px 24px 0 24px; color: #fff;
  }
  .who h2 { font-size: 24px; font-weight: 800; margin-bottom: 10px; }
  .who p { font-size: 14px; line-height: 1.25; font-weight: 600; }
  .services {
    position: absolute; top: 285px; left: 280px; width: 560px; height: 285px;
  }
  .services h2 {
    position: absolute; left: 22px; top: 30px;
    color: var(--orange); font-size: 24px; font-weight: 800;
  }
  .service-list {
    position: absolute; list-style: none; font-size: 13px; line-height: 1.3; color: var(--ink);
  }
  .service-list li { position: relative; padding-left: 12px; margin-bottom: 12px; }
  .service-list li::before {
    content: ""; position: absolute; left: 0; top: 7px;
    width: 5px; height: 5px; background: var(--orange); border-radius: 50%;
  }
  .service-list--left { left: 22px; top: 72px; width: 240px; }
  .service-list--right { left: 300px; top: 40px; width: 240px; }
  .services__divider { position: absolute; left: 280px; top: 30px; width: 1px; height: 230px; background: var(--rule); }
</style>
</head>
<body>

<!-- Outside spread -->
<section class="sheet sheet--outside">
  <div class="panel panel--contact">
    <p class="callout"><strong>Call us</strong> now for a borrowing capacity or <strong>email us</strong> your details and we will call within <strong>24 hours</strong></p>
    <svg class="photo" style="left:0;top:190px" width="280" height="380" role="img" aria-label="Photo of a smiling couple looking at a laptop together">
      <defs><linearGradient id="g-couple" x1="0" y1="0" x2="1" y2="1"><stop offset="0" stop-color="#e8e1d6"/><stop offset=".6" stop-color="#c7a88a"/><stop offset="1" stop-color="#8d7660"/></linearGradient></defs>
      <rect width="280" height="380" fill="url(#g-couple)"/>
    </svg>
    <div class="contact-tab"><span>Contact Us</span></div>
  </div>

  <div class="panel panel--director">
    <div class="portrait" role="img" aria-label="Portrait photo of the director"></div>
    <div class="director">
      <p class="director__name">Tessa Marlow</p>
      <p class="director__company">Quorra Capital</p>
      <p class="director__role">director</p>
    </div>
    <div class="detail detail--phone">
      <svg width="16" height="16" viewBox="0 0 24 24"><path d="M6.6 10.8a15 15 0 0 0 6.6 6.6l2.2-2.2c.3-.3.7-.4 1-.2 1.1.4 2.3.6 3.6.6.6 0 1 .4 1 1V20c0 .6-.4 1-1 1A17 17 0 0 1 3 4c0-.6.4-1 1-1h3.5c.6 0 1 .4 1 1 0 1.3.2 2.5.6 3.6.1.3 0 .7-.2 1z" fill="var(--orange)"/></svg>
      02 8123 4567<br>0411 902 358
    </div>
    <div class="detail detail--address">
      <svg width="14" height="18" viewBox="0 0 24 30"><path d="M12 0a10 10 0 0 0-10 10c0 7.5 10 20 10 20s10-12.5 10-20A10 10 0 0 0 12 0zm0 14a4 4 0 1 1 0-8 4 4 0 0 1 0 8z" fill="var(--orange)"/></svg>
      Level 4, 18 Harbour Lane<br>Ryde NSW 2112
    </div>
    <div class="detail detail--email">
      <svg width="18" height="13" viewBox="0 0 24 17"><rect x="1" y="1" width="22" height="15" rx="1" fill="none" stroke="var(--orange)" stroke-width="2"/><path d="M1 1l11 9 11-9" fill="none" stroke="var(--orange)" stroke-width="2"/></svg>
      tessa@quorracapital.com.au<br>ABN 48213097564
    </div>
    <p class="detail detail--web">www.quorracapital.com.au</p>
  </div>

  <div class="panel panel--cover">
    <svg class="photo" style="left:0;top:0" width="280" height="400" role="img" aria-label="Photo of a happy family standing in front of their new house">
      <defs><linearGradient id="g-family" x1="0" y1="0" x2="0" y2="1"><stop offset="0" stop-color="#d9e4ee"/><stop offset=".5" stop-color="#b8c3c9"/><stop offset="1" stop-color="#5f6b78"/></linearGradient></defs>
      <rect width="280" height="400" fill="url(#g-family)"/>
    </svg>
    <div class="brand"><span class="brand__mark"></span><span class="brand__name">QUORRA CAPITAL</span></div>
    <p class="brand__tagline">Tailored lending &amp; mortgage solutions</p>
    <svg class="cover-swoosh" width="280" height="80" viewBox="0 0 280 80">
      <path d="M0 80 L0 60 Q140 20 280 0 L280 80 Z" fill="var(--orange)"/>
      <path d="M0 60 Q140 20 280 0 L280 12 Q140 32 0 72 Z" fill="var(--orange-light)"/>
    </svg>
  </div>
</section>

<!-- Inside spread -->
<section class="sheet sheet--inside">
  <div class="panel panel--about">
    <div class="who">
      <h2>Who we are?</h2>
      <p>Lorem ipsum dolor sit amet, consectetur adipiscing elit, sed do eiusmod tempor incididunt ut labore et dolore magna aliqua. Ut enim ad minim veniam, quis nostrud exercitation ullamco laboris nisi ut aliquip ex ea commodo consequat. Duis aute irure dolor in reprehenderit in voluptate velit esse cillum dolore eu fugiat nulla pariatur.</p>
    </div>
    <svg class="photo" style="left:0;top:290px" width="280" height="280" role="img" aria-label="Photo of a couple sitting on the floor below sketches of home furnishings">
      <defs><linearGradient id="g-sketch" x1="0" y1="0" x2="0" y2="1"><stop offset="0" stop-color="#f4f4f2"/><stop offset=".55" stop-color="#ddd8d0"/><stop offset="1" stop-color="#9a8f83"/></linearGradient></defs>
      <rect width="280" height="280" fill="url(#g-sketch)"/>
    </svg>
  </div>

  <div class="panel panel--feature" style="width:560px">
    <svg class="photo" style="left:0;top:0" width="560" height="285" role="img" aria-label="Photo of a smiling couple holding a model house with a for sale sign">
      <defs><linearGradient id="g-house" x1="0" y1="0" x2="1" y2="0"><stop offset="0" stop-color="#efe7dc"/><stop offset=".5" stop-color="#d2b08c"/><stop offset="1" stop-color="#8c7b6c"/></linearGradient></defs>
      <rect width="560" height="285" fill="url(#g-house)"/>
      <path d="M0 285 L0 255 Q280 225 560 190 L560 210 Q280 245 0 275 Z" fill="var(--orange)"/>
    </svg>
  </div>

  <div class="services">
    <h2>What we do?</h2>
    <ul class="service-list service-list--left">
      <li>Mortgage solutions tailored to your needs</li>
      <li>Asset Finance solutions</li>
      <li>Commercial/business lending solutions</li>
      <li>We can conduct over the phone interviews to save you time</li>
    </ul>
    <div class="services__divider"></div>
    <ul class="service-list service-list--right">
      <li>We have access to a wide panel of lenders to save you time and do all the legwork for you to save you time and money. We also do not charge a brokerage fee.</li>
      <li>We do not charge you a fee on top of standard bank fees and charges for using our services</li>
    </ul>
  </div>
</section>

</body>
</html>
```